VOIP company busioness card redesign

Redesign business card to match our new logo and marketing material. Should include logo on one side and contact information on other side.

We like modern and clean

Industry/Entity Type

Phone Company

Contact Information for Business Card

One side should be logo other side should include contact info
Name
Phone Number
email
website

Other font styles liked:
• dont care

Requirements
Must have
• Modern sleek design that works with our logo

```html
<!DOCTYPE html>
<html lang="en">
<head>
<meta charset="utf-8">
<title>Corvane Solutions – Business Card</title>
<link rel="stylesheet" href="https://fonts.googleapis.com/css2?family=Arimo:wght@400;700&display=swap">
<style>
  :root {
    --page-bg: #e4e4e4;
    --card-bg: #eef4f4;
    --brand-blue: #1f8fcf;
    --text-grey: #6b6e70;
    --text-dark: #55595b;
    --card-shadow: rgba(0, 0, 0, 0.18);
  }
  * { box-sizing: border-box; margin: 0; padding: 0; }
  html, body {
    width: 1200px;
    height: 1083px;
    overflow: hidden;
    background: var(--page-bg);
    font-family: "Arimo", Arial, sans-serif;
  }
  .stage {
    position: relative;
    width: 1200px;
    height: 1083px;
  }
  .card {
    position: absolute;
    width: 560px;
    height: 320px;
    background: var(--card-bg);
    box-shadow: 0 10px 24px var(--card-shadow);
  }
  .card--front { left: 90px; top: 150px; }
  .card--back  { left: 550px; top: 600px; }

  .brand {
    display: flex;
    align-items: center;
    gap: 10px;
  }
  .brand__dot {
    flex: none;
    border-radius: 50%;
    background: var(--brand-blue);
  }
  .brand__name {
    color: var(--brand-blue);
    font-weight: 400;
    line-height: 1;
    white-space: nowrap;
  }

  .card--front .brand {
    position: absolute;
    left: 50%;
    top: 50%;
    transform: translate(-50%, -50%);
  }
  .card--front .brand__dot { width: 14px; height: 14px; }
  .card--front .brand__name { font-size: 40px; }

  .card--back .brand {
    position: absolute;
    left: 28px;
    top: 40px;
    gap: 7px;
  }
  .card--back .brand__dot { width: 9px; height: 9px; }
  .card--back .brand__name { font-size: 22px; }

  .person {
    position: absolute;
    left: 330px;
    top: 40px;
    color: var(--text-grey);
  }
  .person__name { font-size: 17px; }
  .person__title { font-size: 9px; margin-top: 2px; }

  .contact {
    position: absolute;
    left: 330px;
    top: 215px;
    color: var(--text-grey);
    font-size: 13px;
    line-height: 1.35;
    font-style: normal;
  }
  .contact__phone { font-weight: 700; color: var(--text-dark); }
</style>
</head>
<body>
<main class="stage">
  <section class="card card--front" aria-label="Card front">
    <div class="brand">
      <span class="brand__dot"></span>
      <span class="brand__name">Corvane Solutions</span>
    </div>
  </section>

  <section class="card card--back" aria-label="Card back">
    <div class="brand">
      <span class="brand__dot"></span>
      <span class="brand__name">Corvane Solutions</span>
    </div>

    <div class="person">
      <p class="person__name">Alan Mercer Ross</p>
      <p class="person__title">Sales Manager</p>
    </div>

    <address class="contact">
      <p class="contact__phone">1-855-CORVAN1</p>
      <p>sales@corvanesolutions.com</p>
      <p>www.corvanesolutions.com</p>
    </address>
  </section>
</main>
</body>
</html>
```